Sunny Paths and joy Business card

I have a logo, but will like a business card design. Is for a travel agency in Mexico. We focus in family experiences.

I will liek some thing different and unique, from the traditional business card, something to get remmeber for.

Business card information:

Leandro T. Ocampo
leandro@sunnypathsjoy.example

Alameda 482, 3 piso
Col. Tlalpizco
Mexico, D.F. 07320

office: (55) 5000-0142
mobile: (55) 9000-0187

www.sunnypathsjoy.example
@sunnypjoy
blog: sunnypathsandjoy.blogsite.example
facebook: SunnyPathsAndJoy

```html
<!DOCTYPE html>
<html lang="en">
<head>
<meta charset="utf-8">
<title>Sunny Paths and joy — Business Card</title>
<link rel="stylesheet" href="https://fonts.googleapis.com/css2?family=Open+Sans:wght@400;700&display=swap">
<style>
  :root {
    --backdrop: #4a2e1c;
    --card: #ffffff;
    --brand-blue: #155a82;
    --rule-dark: #2a2a2a;
    --text-grey: #555555;
    --text-dark: #333333;
    --logo-blue: #1f5fa8;
    --logo-sky: #cfe6f5;
  }
  * { margin: 0; padding: 0; box-sizing: border-box; }
  html, body {
    width: 1200px; height: 412px; overflow: hidden;
    background: var(--backdrop);
    font-family: "Open Sans", Arial, sans-serif;
  }
  .stage { position: relative; width: 1200px; height: 412px; }
  .card {
    position: absolute; top: 64px;
    width: 497px; height: 284px;
    background: var(--card);
    box-shadow: 0 3px 8px rgba(0,0,0,.45);
    overflow: hidden;
  }
  .card--front { left: 73px; }
  .card--back { left: 631px; }

  .name-band {
    position: absolute; left: 0; top: 0; width: 100%; height: 53px;
    background: var(--brand-blue);
    color: #fff; font-weight: 700; font-size: 16.5px;
    display: flex; align-items: center; justify-content: center;
  }
  .rule {
    position: absolute; left: 0; width: 100%; height: 3px;
    background: var(--rule-dark);
  }
  .card--front .rule { top: 57px; }
  .card--back .rule { top: 223px; }

  .brand-mark {
    position: absolute; left: 0; width: 100%;
    display: flex; align-items: center; justify-content: center; gap: 10px;
    color: var(--logo-blue); font-weight: 700;
  }
  .brand-mark__dot {
    border-radius: 50%; background: var(--logo-sky); flex: none;
  }
  .card--front .brand-mark { top: 110px; font-size: 19px; }
  .card--front .brand-mark__dot { width: 34px; height: 34px; }
  .card--back .brand-mark { top: 92px; font-size: 23px; }
  .card--back .brand-mark__dot { width: 42px; height: 42px; }

  .address {
    position: absolute; right: 277px; top: 214px;
    text-align: right; font-size: 12.5px; line-height: 17px;
    color: var(--text-grey);
  }
  .divider {
    position: absolute; left: 230px; top: 205px;
    width: 1px; height: 61px; background: var(--text-dark);
  }
  .contact-list {
    position: absolute; left: 256px; top: 204px;
    list-style: none; font-size: 12.5px; line-height: 16.7px;
    color: var(--text-dark);
  }
  .contact-list li { display: flex; align-items: center; gap: 5px; }
  .contact-list svg { width: 9px; height: 9px; flex: none; fill: var(--text-dark); }

  .social-band {
    position: absolute; left: 0; top: 228px; width: 100%; height: 56px;
    background: var(--brand-blue);
    display: flex; align-items: center; justify-content: center; gap: 16px;
    color: #fff; font-size: 13px;
  }
  .social-item { display: flex; align-items: center; gap: 6px; }
  .social-item__badge { width: 17px; height: 17px; background: #fff; border-radius: 3px; }
</style>
</head>
<body>
<div class="stage">

  <section class="card card--front">
    <div class="name-band">Leandro T. Ocampo</div>
    <div class="rule"></div>
    <div class="brand-mark"><span class="brand-mark__dot"></span><span>Sunny Paths and joy</span></div>

    <address class="address" style="font-style:normal">
      Alameda 482, 3 piso<br>
      Col. Tlalpizco<br>
      Mexico, D.F. 07320
    </address>
    <div class="divider"></div>
    <ul class="contact-list">
      <li><svg viewBox="0 0 10 10"><path d="M2 0h2l1 3-1.5 1a6 6 0 0 0 2.5 2.5L7 5l3 1v2c0 1-1 2-2 2A8 8 0 0 1 0 2c0-1 1-2 2-2z"/></svg>(55) 5000-0142</li>
      <li><svg viewBox="0 0 10 10"><rect x="2.5" y="0" width="5" height="10" rx="1"/></svg>(55) 9000-0187</li>
      <li><svg viewBox="0 0 10 10"><path d="M0 2h10v7H0z M0 2l5 4 5-4" stroke="#fff" stroke-width=".8"/></svg>leandro@sunnypathsjoy.example</li>
      <li><svg viewBox="0 0 10 10"><circle cx="5" cy="5" r="5"/></svg>www.sunnypathsjoy.example</li>
    </ul>
  </section>

  <section class="card card--back">
    <div class="brand-mark"><span class="brand-mark__dot"></span><span>Sunny Paths and joy</span></div>
    <div class="rule"></div>
    <div class="social-band">
      <span class="social-item"><span class="social-item__badge"></span>sunnypathsandjoy.blogsite.example</span>
      <span class="social-item"><span class="social-item__badge"></span>SunnyPathsAndJoy</span>
    </div>
  </section>

</div>
</body>
</html>
```